Waste Oil Filter collection & disposal

Basically I need a 1 page website for the business called Grennick Waste Partners.
We are a environmental service provider and we collect and dispose of waste oil filters to protect the environment from hazardous waste oil products.

This is the link to our current website: www.grennickwaste.co.nz

we want it to look fresh and better than our current website. we may potentially look at getting a new logo designed and are open to ideas/designs if you have any.

Industry/Entity Type

Business

Logo Text

Grennick Waste Partners

Number of Pages Required

1 page

Requirements
Must have
• same colours as current website.
• description of what service we provide please refer to leaflet attached

```html
<!DOCTYPE html>
<html lang="en">
<head>
<meta charset="utf-8">
<title>Grennick Waste Partners — Oil Filter Collection &amp; Disposal</title>
<link href="https://fonts.googleapis.com/css2?family=Open+Sans:wght@400;600;700&family=PT+Sans+Narrow&display=swap" rel="stylesheet">
<style>
:root{
  --brand-blue:#2f6fb8;
  --heading:#444444;
  --body:#4a4a4a;
  --white:#ffffff;
  --soft-bg:#f6f7f8;
  --footer:#3b3b3b;
  --gold:#d8a21a;
  --purple:#8e44ad;
  --slate:#7f9c96;
  --amber:#f5b21b;
  --green:#6cb04a;
  --teal:#17b89b;
  --sky:#2d9fd9;
}
*{margin:0;padding:0;box-sizing:border-box}
html,body{width:1200px;height:3000px;overflow:hidden;background:var(--white)}
body{position:relative;font-family:"Open Sans",sans-serif;color:var(--body)}
.abs{position:absolute}

.hero{left:0;top:0;width:1200px;height:740px;
  background:linear-gradient(135deg,#2b2b2b 0%,#5a5a5a 35%,#8a5a4a 55%,#b04a3a 70%,#6b6b6b 100%)}
.hero-shade{left:0;top:0;width:1200px;height:740px;background:rgba(0,0,0,.25)}
.nav{left:0;top:0;width:1200px;height:64px;display:flex;align-items:center;justify-content:space-between;padding:0 56px 0 62px}
.brand{font-size:31px;font-weight:700;color:var(--brand-blue);white-space:nowrap}
.nav-links{display:flex;gap:38px;font-size:24px;color:var(--white)}
.hero-title{left:444px;top:294px;font-size:54px;font-weight:700;line-height:1.2;color:var(--white);white-space:nowrap;text-shadow:2px 3px 6px rgba(0,0,0,.6)}
.hero-sub{left:444px;top:384px;font-size:34px;color:var(--white);white-space:nowrap}
.scroll-down{left:590px;top:646px}

.photo{border-radius:2px}
.brick-photo{left:58px;top:774px;width:404px;height:402px;background:linear-gradient(160deg,#7c8a99,#3e4752 50%,#9b6b4a)}
.h2{font-size:64px;font-weight:700;color:var(--heading);line-height:1.12}
.lead{font-size:28px;line-height:1.3;color:var(--body)}
.brick-title{left:584px;top:868px}
.brick-text{left:516px;top:960px;width:640px}
.process-title{left:54px;top:1262px}
.process-text{left:56px;top:1418px;width:640px}
.process-photo{left:738px;top:1218px;width:408px;height:348px;background:linear-gradient(150deg,#9aa3a8,#4d5a5f 45%,#2f7a66 65%,#555)}

.machine-photo{left:398px;top:1570px;width:424px;height:432px;background:linear-gradient(180deg,#e0562a 0%,#d9502a 55%,#4a4a4a 80%,#2a2a2a 100%);border-radius:20px 20px 6px 6px}
.feature-icon{width:40px;height:40px;border-radius:50%;display:flex;align-items:center;justify-content:center}
.feature-icon i{width:16px;height:16px;border:3px solid var(--white);border-radius:3px}
.feature-text{width:270px;font-size:15px;line-height:1.32;color:#333}
.feature-text.left{text-align:right}

.demo-band{left:0;top:2064px;width:1200px;height:494px;background:var(--soft-bg)}
.demo-title{left:0;top:2052px;width:1200px;text-align:center;font-size:62px;font-weight:700;line-height:1.15;color:var(--heading)}
.demo-sub{left:180px;top:2124px;width:840px;text-align:center;font-size:21px;line-height:1.25;font-weight:600;color:#666}
.video{left:268px;top:2190px;width:670px;height:324px;background:#000;display:flex;align-items:center;justify-content:center}

.feedback-title{left:0;top:2540px;width:1200px;text-align:center;font-size:62px;font-weight:700;color:var(--heading)}
.quote{width:362px;font-family:"PT Sans Narrow",sans-serif;font-size:18px;line-height:1.65;color:#333}
.client{display:flex;align-items:center;gap:8px}
.avatar{width:48px;height:48px;border-radius:50%;background:linear-gradient(160deg,#9aa5ad,#5d6670)}
.client-name{font-family:"PT Sans Narrow",sans-serif;font-size:17px;color:#333;white-space:nowrap}
.stars{display:flex;gap:2px;margin-top:2px}

.to-top{left:1144px;top:2866px;width:40px;height:40px;border-radius:50%;background:#c9c9c9;display:flex;align-items:center;justify-content:center}
.footer{left:0;top:2932px;width:1200px;height:68px;background:var(--footer);display:flex;align-items:center;justify-content:space-between;padding:0 56px 0 76px}
.copyright{font-size:20px;font-weight:700;color:var(--white)}
.social{display:flex;gap:22px}
.social span{width:20px;height:20px;border-radius:50%;background:var(--amber)}
</style>
</head>
<body>

<section class="abs hero" role="img" aria-label="Photo of used oil filters collected in a bin, with a black filter in the foreground"></section>
<div class="abs hero-shade"></div>

<header class="abs nav">
  <div class="brand">Grennick Waste Partners Ltd</div>
  <nav class="nav-links"><span>HOME</span><span>FEATURES</span><span>CLIENTS</span><span>CONTACT</span></nav>
</header>

<h1 class="abs hero-title">Grennick Waste Partners</h1>
<p class="abs hero-sub">Oil Filter Collection &amp; Disposal Service</p>
<svg class="abs scroll-down" width="72" height="72" viewBox="0 0 72 72" aria-hidden="true">
  <circle cx="36" cy="36" r="32" fill="none" stroke="#fff" stroke-width="3"/>
  <polyline points="24,26 36,38 48,26" fill="none" stroke="#fff" stroke-width="3"/>
  <polyline points="24,36 36,48 48,36" fill="none" stroke="#fff" stroke-width="3"/>
</svg>

<div class="abs photo brick-photo" role="img" aria-label="Photo of a compressed brick of used oil filters strapped on a pallet"></div>
<h2 class="abs h2 brick-title">Brick of filters</h2>
<p class="abs lead brick-text">Conveniently whiteboard prospect catalysts for change without principle centeredempower.</p>

<h2 class="abs h2 process-title">Filter processing<br>machine</h2>
<p class="abs lead process-text">Conveniently whiteboard prospect catalysts for change without principle centeredempower.</p>
<div class="abs photo process-photo" role="img" aria-label="Photo of a green filter processing machine in a workshop"></div>

<div class="abs feature-icon" style="left:270px;top:1602px;background:var(--purple)"><i></i></div>
<p class="abs feature-text left" style="left:50px;top:1656px">Conveniently whitebo prospect and to perform catalysts change without principle centered to done power.</p>
<div class="abs feature-icon" style="left:270px;top:1750px;background:var(--slate)"><i></i></div>
<p class="abs feature-text left" style="left:50px;top:1804px">Conveniently whitebo prospect and to perform catalysts change without principle centered to done power.</p>
<div class="abs feature-icon" style="left:270px;top:1904px;background:var(--amber)"><i></i></div>
<p class="abs feature-text left" style="left:50px;top:1958px">Conveniently whitebo prospect and to perform catalysts change without principle centered to done power.</p>

<div class="abs machine-photo" role="img" aria-label="Photo of an orange Torvale industrial filter crushing unit on wheels"></div>

<div class="abs feature-icon" style="left:900px;top:1600px;background:var(--green)"><i></i></div>
<p class="abs feature-text" style="left:900px;top:1656px">Conveniently whitebo prospect and to perform catalysts change without principle centered to done power.</p>
<div class="abs feature-icon" style="left:900px;top:1752px;background:var(--teal)"><i></i></div>
<p class="abs feature-text" style="left:900px;top:1822px">Conveniently whitebo prospect and to perform catalysts change without principle centered to done power.</p>
<div class="abs feature-icon" style="left:900px;top:1902px;background:var(--sky)"><i></i></div>
<p class="abs feature-text" style="left:900px;top:1966px">Conveniently whitebo prospect and to perform catalysts change without principle centered to done power.</p>

<section class="abs demo-band"></section>
<h2 class="abs demo-title">See a Demo</h2>
<p class="abs demo-sub">Conveniently whiteboard prospect catalysts for change without principle<br>centere empower.</p>
<div class="abs video">
  <svg width="72" height="72" viewBox="0 0 72 72" aria-label="Play video">
    <circle cx="36" cy="36" r="32" fill="none" stroke="#c9a24a" stroke-width="2.5"/>
    <polygon points="30,26 46,36 30,46" fill="none" stroke="#c9a24a" stroke-width="2.5"/>
  </svg>
</div>

<h2 class="abs feedback-title">Client’s Feedback</h2>

<p class="abs quote" style="left:52px;top:2664px">"Holisticly empower leveraged ROI whereas effective web-readiness. Completely enable emerging meta-services with cross-platform web services. Quickly initi ate inexpensiveios.</p>
<p class="abs quote" style="left:428px;top:2664px">"Holisticly empower leveraged ROI whereas effective web-readiness. Completely enable emerging meta-services with cross-platform web services. Quickly initi ate inexpensiveios.</p>
<p class="abs quote" style="left:804px;top:2664px">"Holisticly empower leveraged ROI whereas effective web-readiness. Completely enable emerging meta-services with cross-platform web services. Quickly initi ate inexpensiveios.</p>

<div class="abs client" style="left:52px;top:2826px">
  <div class="avatar" role="img" aria-label="Client portrait"></div>
  <div><div class="client-name">Martin Holloway, Kestrel Freight co.</div>
  <svg class="stars" width="80" height="16" viewBox="0 0 80 16" aria-label="Five stars"><g fill="#d8a21a"><polygon points="8,1 10,6 15,6 11,9.5 12.5,15 8,11.7 3.5,15 5,9.5 1,6 6,6"/><polygon transform="translate(16 0)" points="8,1 10,6 15,6 11,9.5 12.5,15 8,11.7 3.5,15 5,9.5 1,6 6,6"/><polygon transform="translate(32 0)" points="8,1 10,6 15,6 11,9.5 12.5,15 8,11.7 3.5,15 5,9.5 1,6 6,6"/><polygon transform="translate(48 0)" points="8,1 10,6 15,6 11,9.5 12.5,15 8,11.7 3.5,15 5,9.5 1,6 6,6"/><polygon transform="translate(64 0)" points="8,1 10,6 15,6 11,9.5 12.5,15 8,11.7 3.5,15 5,9.5 1,6 6,6"/></g></svg></div>
</div>
<div class="abs client" style="left:412px;top:2826px">
  <div class="avatar" role="img" aria-label="Client portrait"></div>
  <div><div class="client-name">Martin Holloway, Kestrel Freight co.</div>
  <svg class="stars" width="80" height="16" viewBox="0 0 80 16" aria-label="Five stars"><g fill="#d8a21a"><polygon points="8,1 10,6 15,6 11,9.5 12.5,15 8,11.7 3.5,15 5,9.5 1,6 6,6"/><polygon transform="translate(16 0)" points="8,1 10,6 15,6 11,9.5 12.5,15 8,11.7 3.5,15 5,9.5 1,6 6,6"/><polygon transform="translate(32 0)" points="8,1 10,6 15,6 11,9.5 12.5,15 8,11.7 3.5,15 5,9.5 1,6 6,6"/><polygon transform="translate(48 0)" points="8,1 10,6 15,6 11,9.5 12.5,15 8,11.7 3.5,15 5,9.5 1,6 6,6"/><polygon transform="translate(64 0)" points="8,1 10,6 15,6 11,9.5 12.5,15 8,11.7 3.5,15 5,9.5 1,6 6,6"/></g></svg></div>
</div>
<div class="abs client" style="left:796px;top:2826px">
  <div class="avatar" role="img" aria-label="Client portrait"></div>
  <div><div class="client-name">Martin Holloway, Kestrel Freight co.</div>
  <svg class="stars" width="80" height="16" viewBox="0 0 80 16" aria-label="Five stars"><g fill="#d8a21a"><polygon points="8,1 10,6 15,6 11,9.5 12.5,15 8,11.7 3.5,15 5,9.5 1,6 6,6"/><polygon transform="translate(16 0)" points="8,1 10,6 15,6 11,9.5 12.5,15 8,11.7 3.5,15 5,9.5 1,6 6,6"/><polygon transform="translate(32 0)" points="8,1 10,6 15,6 11,9.5 12.5,15 8,11.7 3.5,15 5,9.5 1,6 6,6"/><polygon transform="translate(48 0)" points="8,1 10,6 15,6 11,9.5 12.5,15 8,11.7 3.5,15 5,9.5 1,6 6,6"/><polygon transform="translate(64 0)" points="8,1 10,6 15,6 11,9.5 12.5,15 8,11.7 3.5,15 5,9.5 1,6 6,6"/></g></svg></div>
</div>

<div class="abs to-top" aria-label="Back to top">
  <svg width="18" height="12" viewBox="0 0 18 12"><polyline points="3,9 9,3 15,9" fill="none" stroke="#fff" stroke-width="3"/></svg>
</div>

<footer class="abs footer">
  <span class="copyright">@2017. All Rights Reserved.</span>
  <div class="social" aria-label="Social links"><span></span><span></span><span></span></div>
</footer>

</body>
</html>
```